Larkspur Ridge Management - Business Cards

I need business cards. My current logo was designed by a designer at this site and I very much like and am happy with the results. I would like a business card that is trendy, unique, current yet professional. I deal with high net worth clients daily

Target Market(s)

Out of state investors looking to get into the rental market in Ohio

Industry/Entity Type

Property Management, Consulting

Contact Information for Business Card

Name, Title (Chief Financial Officer) office phone number (555) 817-3094 website address larkridgemgmt.example

Font styles to use
Sans Serif

Colors
0054AA
0677BA
7BADD7
CADEEF
E8F1F8
0094D4
00A9DD
6FCCEA
C7EBF8
E9F6FB
00AB8E
00BBA5
67D7C9
C6EFE9
E9F9F6

```html
<!DOCTYPE html>
<html lang="en">
<head>
<meta charset="utf-8">
<title>Larkspur Ridge Management – Business Cards</title>
<link rel="stylesheet" href="https://fonts.googleapis.com/css2?family=Montserrat:wght@400;500;600;700;800&display=swap">
<style>
  :root {
    --brand-blue: #0054AA;
    --brand-blue-mid: #0677BA;
    --brand-sky: #00A9DD;
    --brand-teal: #00AB8E;
    --paper: #E8F1F8;
    --ink: #0054AA;
    --muted: #0677BA;
    --white: #ffffff;
    --backdrop: #8f9ba4;
  }
  * { margin: 0; padding: 0; box-sizing: border-box; }
  html, body {
    width: 1200px;
    height: 1038px;
    overflow: hidden;
    background: var(--backdrop);
    font-family: "Montserrat", sans-serif;
  }
  .stage { position: relative; width: 1200px; height: 1038px; }

  .card {
    position: absolute;
    width: 640px;
    height: 366px;
    overflow: hidden;
  }

  /* Front */
  .card-front {
    left: 100px;
    top: 110px;
    background: var(--brand-blue);
    display: flex;
    align-items: center;
    justify-content: center;
  }
  .front-wordmark {
    display: flex;
    align-items: center;
    gap: 14px;
    color: var(--white);
    font-weight: 800;
    font-size: 30px;
    letter-spacing: 1px;
    text-transform: uppercase;
    line-height: 1.1;
  }
  .front-wordmark .mark-square {
    width: 22px;
    height: 22px;
    background: var(--white);
    flex: none;
  }

  /* Back */
  .card-back {
    left: 460px;
    top: 560px;
    background: var(--paper);
  }
  .back-band {
    position: absolute;
    inset: 0;
    width: 640px;
    height: 366px;
  }
  .back-wordmark {
    position: absolute;
    left: 38px;
    top: 236px;
    color: var(--ink);
    font-weight: 800;
    font-size: 15px;
    letter-spacing: 0.5px;
    text-transform: uppercase;
    line-height: 1.2;
  }
  .contact {
    position: absolute;
    left: 300px;
    top: 56px;
    color: var(--ink);
  }
  .contact-name {
    font-weight: 700;
    font-size: 30px;
    line-height: 1;
  }
  .contact-title {
    margin-top: 10px;
    font-size: 7px;
    font-weight: 500;
    letter-spacing: 1px;
    color: var(--muted);
    text-transform: uppercase;
  }
  .contact-list {
    list-style: none;
    margin-top: 18px;
  }
  .contact-item {
    display: flex;
    align-items: flex-start;
    gap: 10px;
    font-size: 14px;
    font-weight: 500;
    line-height: 1.3;
    margin-bottom: 10px;
  }
  .contact-item.address { font-size: 11px; }
  .contact-icon {
    width: 16px;
    height: 16px;
    flex: none;
    margin-top: 1px;
  }
</style>
</head>
<body>
<main class="stage">

  <section class="card card-front" aria-label="Business card front">
    <div class="front-wordmark">
      <span class="mark-square"></span>
      <span>Larkspur Ridge<br>Management</span>
    </div>
  </section>

  <section class="card card-back" aria-label="Business card back">
    <svg class="back-band" viewBox="0 0 640 366" aria-hidden="true">
      <polygon points="0,336 640,232 640,366 0,366" fill="var(--brand-blue)"/>
      <polygon points="0,336 640,232 640,238 0,342" fill="var(--brand-sky)"/>
    </svg>

    <div class="back-wordmark">Larkspur Ridge<br>Management</div>

    <div class="contact">
      <h1 class="contact-name">Daniel Harlow</h1>
      <p class="contact-title">Chief Financial Officer</p>
      <ul class="contact-list">
        <li class="contact-item">
          <svg class="contact-icon" viewBox="0 0 16 16" aria-hidden="true">
            <circle cx="8" cy="8" r="7.2" fill="none" stroke="var(--ink)" stroke-width="1.1"/>
            <path d="M5.4 4.6 L6.6 4.4 L7.2 6 L6.4 6.7 Q7 8.4 9.2 9.6 L9.9 8.8 L11.5 9.4 L11.3 10.7 Q8.5 11.3 6.3 9 Q4.5 7 5.4 4.6 Z" fill="var(--ink)"/>
          </svg>
          <span>(555) 817-3094</span>
        </li>
        <li class="contact-item">
          <svg class="contact-icon" viewBox="0 0 16 16" aria-hidden="true">
            <circle cx="8" cy="8" r="7.2" fill="none" stroke="var(--ink)" stroke-width="1.1"/>
            <rect x="4.3" y="5.5" width="7.4" height="5" fill="none" stroke="var(--ink)" stroke-width="1"/>
            <path d="M4.3 5.5 L8 8.4 L11.7 5.5" fill="none" stroke="var(--ink)" stroke-width="1"/>
          </svg>
          <span>info@larkridgemgmt.example</span>
        </li>
        <li class="contact-item">
          <svg class="contact-icon" viewBox="0 0 16 16" aria-hidden="true">
            <circle cx="8" cy="8" r="7.2" fill="none" stroke="var(--ink)" stroke-width="1.1"/>
            <circle cx="8" cy="8" r="3.6" fill="none" stroke="var(--ink)" stroke-width="1"/>
            <path d="M4.4 8 H11.6 M8 4.4 Q6.2 8 8 11.6 M8 4.4 Q9.8 8 8 11.6" fill="none" stroke="var(--ink)" stroke-width="0.8"/>
          </svg>
          <span>larkridgemgmt.example</span>
        </li>
        <li class="contact-item address">
          <svg class="contact-icon" viewBox="0 0 16 16" aria-hidden="true">
            <circle cx="8" cy="8" r="7.2" fill="none" stroke="var(--ink)" stroke-width="1.1"/>
            <path d="M8 12 Q5 8.6 5 6.8 A3 3 0 0 1 11 6.8 Q11 8.6 8 12 Z" fill="var(--ink)"/>
            <circle cx="8" cy="6.8" r="1.1" fill="var(--paper)"/>
          </svg>
          <span>#204-206, 1450 Maple Ave, Fairview,<br>OH 44000</span>
        </li>
      </ul>
    </div>
  </section>

</main>
</body>
</html>
```